Kestrel Bridge Consulting (KBC) Business Card Design

I would like to create double-sided business cards that contain:
1) Name: Derek Molvane
2) Phone Number: +1 (555) 218-4907
3) Email: Derek.Molvane@KestrelBridgeConsulting.example
4) Website: KestrelBridgeConsulting.example

I would like to include my logo and a color scheme similar to the Varnholt Grand Prix Ostera squad color scheme (black, silver, greenish-blue – but can also include regular blue)

What we do: Our company develops and delivers innovative and pragmatic information technology and cybersecurity risk and compliance solutions for organizations in the commercial market as well as the federal, and state/local sectors.

```html
<!DOCTYPE html>
<html lang="en">
<head>
<meta charset="utf-8">
<title>Kestrel Bridge Consulting – Business Card</title>
<link rel="stylesheet" href="https://fonts.googleapis.com/css2?family=Open+Sans:wght@400;500;700&display=swap">
<style>
  :root {
    --backdrop: #8e9da6;
    --paper: #ffffff;
    --ink: #000000;
    --teal: #0acfc5;
    --blue: #0772ae;
    --faint-teal: #033f3c;
    --faint-blue: #01233a;
  }
  * { box-sizing: border-box; margin: 0; padding: 0; }
  html, body {
    width: 1200px; height: 1200px; overflow: hidden;
    background: var(--backdrop);
    font-family: "Open Sans", sans-serif;
  }
  .card {
    position: absolute; left: 206px; width: 789px; height: 451px; overflow: hidden;
  }
  .card--front { top: 121px; background: var(--paper); }
  .card--back { top: 628px; background: var(--ink); }
  .card__art { position: absolute; inset: 0; }

  .holder { position: absolute; left: 49px; top: 42px; color: var(--ink); }
  .holder__name { font-size: 39px; font-weight: 700; letter-spacing: -0.5px; line-height: 1.1; }
  .holder__title { font-size: 24px; font-weight: 500; margin-top: 4px; margin-left: 2px; }

  .contacts { position: absolute; left: 45px; top: 225px; list-style: none; }
  .contact { display: flex; align-items: center; height: 40px; margin-bottom: 30px; }
  .contact__icon {
    width: 40px; height: 40px; border-radius: 50%; flex: none;
    display: flex; align-items: center; justify-content: center;
  }
  .contact__icon--teal { background: var(--teal); }
  .contact__icon--blue { background: var(--blue); }
  .contact__icon svg { width: 18px; height: 18px; }
  .contact__text {
    margin-left: 21px; font-size: 19px; letter-spacing: 0.8px; line-height: 1.3; color: var(--ink);
  }

  .brand {
    position: absolute; display: flex; flex-direction: column; align-items: center;
    color: var(--teal); font-weight: 700; text-align: center; line-height: 1.15;
  }
  .brand__dot { width: 34px; height: 34px; border-radius: 50%; background: var(--teal); margin-bottom: 10px; }
  .brand--front { left: 526px; top: 172px; width: 160px; font-size: 22px; }
  .brand--back { left: 294px; top: 160px; width: 200px; font-size: 26px; }

  .watermark {
    position: absolute; top: 110px; font-size: 230px; font-weight: 700;
    color: var(--faint-teal); line-height: 1; letter-spacing: -4px;
  }
  .watermark--left { left: -190px; }
  .watermark--right { right: -190px; }
</style>
</head>
<body>

<section class="card card--front" aria-label="Business card front">
  <svg class="card__art" viewBox="0 0 789 451" aria-hidden="true">
    <path d="M378 178 L362 201 Q352 216 356 232 L414 451 L470 451 L400 200 Z" fill="var(--blue)"/>
    <path d="M457 0 L789 0 L789 451 L443 451 L363 172 Q358 155 368 140 Z" fill="var(--ink)"/>
    <path d="M487 0 L384 150 Q377 160 380 172 L465 451" fill="none" stroke="var(--teal)" stroke-width="7"/>
  </svg>

  <div class="holder">
    <h1 class="holder__name">Derek Molvane</h1>
    <p class="holder__title">Owner/Founder</p>
  </div>

  <ul class="contacts">
    <li class="contact">
      <span class="contact__icon contact__icon--teal">
        <svg viewBox="0 0 24 24"><path fill="#fff" d="M6.6 10.8a15.1 15.1 0 0 0 6.6 6.6l2.2-2.2a1 1 0 0 1 1-.25 11.4 11.4 0 0 0 3.6.57 1 1 0 0 1 1 1V20a1 1 0 0 1-1 1A17 17 0 0 1 3 4a1 1 0 0 1 1-1h3.5a1 1 0 0 1 1 1c0 1.25.2 2.45.57 3.57a1 1 0 0 1-.25 1z"/></svg>
      </span>
      <span class="contact__text">+1 (555) 218-4907</span>
    </li>
    <li class="contact">
      <span class="contact__icon contact__icon--blue">
        <svg viewBox="0 0 24 24"><rect x="3" y="5" width="18" height="14" rx="2" fill="#fff"/><path d="M3.5 6.5 12 13l8.5-6.5" fill="none" stroke="var(--blue)" stroke-width="1.8"/></svg>
      </span>
      <span class="contact__text">Derek.Molvane@Kestrel<br>BridgeConsulting.example</span>
    </li>
    <li class="contact">
      <span class="contact__icon contact__icon--teal">
        <svg viewBox="0 0 24 24" fill="none" stroke="#fff" stroke-width="1.6"><circle cx="12" cy="12" r="9"/><ellipse cx="12" cy="12" rx="4" ry="9"/><path d="M3 12h18M4.5 7.5h15M4.5 16.5h15"/></svg>
      </span>
      <span class="contact__text">KestrelBridge<br>Consulting.example</span>
    </li>
  </ul>

  <div class="brand brand--front">
    <span class="brand__dot"></span>
    <span>Kestrel Bridge Consulting</span>
  </div>
</section>

<section class="card card--back" aria-label="Business card back">
  <span class="watermark watermark--left" aria-hidden="true">KBC</span>
  <span class="watermark watermark--right" aria-hidden="true">KBC</span>
  <div class="brand brand--back">
    <span class="brand__dot"></span>
    <span>Kestrel Bridge Consulting</span>
  </div>
</section>

</body>
</html>
```